Velmora Care! Create an exciting flyer for our hemodialysis clinic

Create an engaging Flyer that shows our offering and that will drive patients to our hemodialysis clinic. www.velmoracare.example

Target Market(s)

Mass public

Industry/Entity Type

Healthcare

Requirements
Must have
• 1 Our logo. 2. Should include that we accept all insurances 3. Our tag line “Transforming Lives, One Dialysis Session at a Time.”

```html
<!DOCTYPE html>
<html lang="en">
<head>
<meta charset="utf-8">
<title>Velmora Care – Hemodialysis Flyer</title>
<link href="https://fonts.googleapis.com/css2?family=Roboto:wght@400;500;700&family=Roboto+Condensed:wght@700&display=swap" rel="stylesheet">
<style>
  :root{
    --blue:#2e7fbf;
    --green:#58a845;
    --teal:#3f8f8a;
    --dark:#262626;
    --white:#ffffff;
    --page:#d9d9d9;
    --text-dark:#1e1e1e;
  }
  *{box-sizing:border-box;margin:0;padding:0}
  html,body{width:1200px;height:1200px;overflow:hidden;background:var(--page);font-family:"Roboto",Arial,sans-serif}
  .flyer{position:absolute;left:182px;top:63px;width:835px;height:1074px;background:var(--white);overflow:hidden;box-shadow:0 4px 14px rgba(0,0,0,.2)}

  /* hero */
  .hero{position:absolute;left:0;top:0;width:835px;height:441px;
    background:linear-gradient(160deg,#b9cfd6 0%,#9fbfa6 35%,#5f9460 65%,#3f7a45 100%)}
  .hero-fade{position:absolute;left:0;top:0;width:470px;height:441px;
    background:linear-gradient(90deg,rgba(255,255,255,.55),rgba(255,255,255,0))}
  .brand{position:absolute;left:20px;top:26px;width:180px;text-align:center}
  .brand-mark{width:70px;height:70px;background:var(--teal);margin:0 auto 14px}
  .brand-name{font-weight:700;font-size:24px;color:var(--blue);letter-spacing:1px;line-height:1.1;white-space:nowrap}
  .hero-photo{position:absolute;left:262px;top:27px;width:550px;height:395px;border-radius:198px;
    border:5px solid var(--white);background:linear-gradient(120deg,#cfd8de 0%,#6f9fd0 40%,#8fa4b4 70%,#c9d3da 100%)}
  .tagline-box{position:absolute;left:0;top:179px;width:293px;height:128px;
    background:linear-gradient(90deg,var(--blue),var(--green));padding:10px 0 0 24px;color:var(--white);font-family:"Roboto Condensed","Roboto",sans-serif;font-weight:700}
  .tagline-top{font-size:35px;line-height:1}
  .tagline-main{font-size:95px;line-height:.86;letter-spacing:-1px}
  .tagline-sub{position:absolute;left:24px;top:314px;font-size:27px;line-height:1.2;color:var(--text-dark)}

  /* divider */
  .divider{position:absolute;left:0;top:460px;width:835px;height:2px;background:linear-gradient(90deg,var(--blue),var(--green))}
  .divider-bar{position:absolute;left:247px;top:456px;width:341px;height:10px;background:linear-gradient(90deg,var(--blue),var(--green))}

  /* service panels */
  .panel{position:absolute;top:479px;height:309px;color:var(--white);text-align:center}
  .panel-about{left:0;width:418px;background:var(--blue)}
  .panel-dialysis{left:418px;width:417px;background:var(--green)}
  .panel-icon{position:absolute;left:50%;top:16px;width:66px;height:66px;transform:translateX(-50%);border-radius:8px;background:rgba(255,255,255,.2)}
  .panel-title{position:absolute;left:45px;top:101px;width:347px;height:38px;border-radius:19px;background:var(--white);
    font-family:"Roboto Condensed","Roboto",sans-serif;font-weight:700;font-size:29px;line-height:38px;white-space:nowrap}
  .panel-about .panel-title{color:var(--blue)}
  .panel-dialysis .panel-title{left:27px;color:var(--green)}
  .panel-text{position:absolute;left:34px;top:152px;width:366px;font-size:16.5px;line-height:21.2px;letter-spacing:.15px;text-align:justify;text-align-last:center}
  .panel-dialysis .panel-text{left:18px}

  /* partner note */
  .note{position:absolute;left:26px;top:802px;width:783px;height:43px;border:1.5px solid var(--teal);border-radius:10px;
    font-size:16px;line-height:25px;padding-top:5px;text-align:center;color:var(--text-dark)}
  .note-line2{display:inline-block;background:var(--white);padding:0 14px}
  .note-dot{display:inline-block;width:9px;height:9px;border-radius:50%;background:var(--teal);vertical-align:middle;margin:0 8px}

  .insurance{position:absolute;left:268px;top:867px;width:309px;height:37px;border-radius:8px;
    background:linear-gradient(90deg,var(--blue),var(--green));color:var(--white);font-weight:500;font-size:27px;line-height:37px;text-align:center;
    box-shadow:0 8px 10px rgba(0,0,0,.25)}

  /* footer */
  .footer-shape{position:absolute;left:0;top:929px;width:835px;height:145px}
  .footer-call{position:absolute;left:0;top:946px;width:835px;text-align:center;color:var(--white);font-size:16px}
  .footer-call span{display:inline-block;padding:0 4px 6px;border-bottom:1px dashed var(--white)}
  .contacts{position:absolute;left:0;top:990px;width:835px;display:flex;justify-content:space-between;padding:0 32px 0 35px;color:var(--white);font-weight:500;font-size:21px}
  .contact{display:flex;align-items:center;gap:8px}
  .address{position:absolute;left:0;top:1038px;width:835px;text-align:center;color:var(--white);font-size:13px}
  .address::before,.address::after{content:"";display:inline-block;width:40px;height:2px;background:var(--green);vertical-align:middle;margin:0 18px}
</style>
</head>
<body>
<main class="flyer">
  <section class="hero">
    <div class="hero-fade" role="img" aria-label="Tropical coastline of Tobago with green hills and sea"></div>
    <div class="brand">
      <div class="brand-mark"></div>
      <div class="brand-name">VELMORA CARE</div>
    </div>
    <div class="hero-photo" role="img" aria-label="Nurse checking the blood pressure of a patient resting in a treatment chair"></div>
    <div class="tagline-box">
      <div class="tagline-top">TRANSFORMING</div>
      <div class="tagline-main">LIVES</div>
    </div>
    <p class="tagline-sub">One Dialysis Session<br>at a Time</p>
  </section>

  <div class="divider"></div>
  <div class="divider-bar"></div>

  <section class="panel panel-about">
    <div class="panel-icon" role="img" aria-label="Icon of a group of people"></div>
    <h2 class="panel-title">ABOUT US</h2>
    <p class="panel-text">Velmora Care is Tobago's 1st and pioneering private dialysis facility. Velmora Care is proud to be part of healthcare landscape in Tobago providing support to Tobago's excellent public healthcare dialysis facilities, to meet the needs of both local, regional and international patients.</p>
  </section>

  <section class="panel panel-dialysis">
    <div class="panel-icon" role="img" aria-label="Icon of a dialysis machine"></div>
    <h2 class="panel-title">IN-CENTER HEMODIALYSIS</h2>
    <p class="panel-text">We offer In-center hemodialysis for renal patients who prefer to have their treatments at a dialysis center. Our dialysis center has 6 Aurelis dialysis machines, supported by our state of the art water purification system. Pick up and drop off of patients is an additional service we offer for all in-center hemodialysis patients.</p>
  </section>

  <div class="note">
    Once you're a dialysis patient with Velmora, you can also dialyze at any or our partner locations in Trinidad<br>
    <span class="note-line2"><span class="note-dot"></span>(Chaguanas and Piarco).<span class="note-dot"></span></span>
  </div>

  <div class="insurance">We accept all insurances</div>

  <svg class="footer-shape" width="835" height="145" viewBox="0 0 835 145" preserveAspectRatio="none">
    <path d="M0 58 Q417.5 -58 835 58 V145 H0 Z" fill="#262626"/>
  </svg>
  <p class="footer-call"><span>Please give us a call or email to schedule the service</span></p>
  <div class="contacts">
    <div class="contact">
      <svg width="18" height="16" viewBox="0 0 18 16"><path d="M0 8 18 0 12 16 9 10Z" fill="#58a845"/></svg>
      info@velmoracare.example
    </div>
    <div class="contact">
      <svg width="18" height="18" viewBox="0 0 24 24" fill="none" stroke="#58a845" stroke-width="2.2"><path d="M5 3h4l2 5-3 2a11 11 0 0 0 6 6l2-3 5 2v4a2 2 0 0 1-2 2A17 17 0 0 1 3 5a2 2 0 0 1 2-2z"/></svg>
      868-555-0142
    </div>
    <div class="contact">
      <svg width="18" height="18" viewBox="0 0 24 24" fill="none" stroke="#58a845" stroke-width="2"><circle cx="12" cy="12" r="10"/><path d="M2 12h20M12 2c3 3 3 17 0 20M12 2c-3 3-3 17 0 20"/></svg>
      www.velmoracare.example
    </div>
  </div>
  <p class="address">14 Palm Crest Lane, Off Harbour Road, Bay View, Mt. Serene</p>
</main>
</body>
</html>
```